Infographic representing workforce

Hello - I would like an infographic created to insert into a document to represent the composition of our workforce.
I've attached one very casual idea below but do NOT like the pink! Would prefer something a little more professional / modern.
Here is the information:
TOTAL EMPLOYEES
25
DIVERSITY
White: 60%
Asian: 24%
Hispanic: 8%
Middle-Eastern: 8%
AGE
25 - 44: 32%
45 - 64: 56%
65+: 12%
GENDER
Female: 60%
Male: 40%
EXECUTIVE OFFICERS
2of 3 are women
BOARD COMPOSITION
50% women (3 directors)
One woman from an unrepresented community

```html
<!DOCTYPE html>
<html lang="en">
<head>
<meta charset="utf-8">
<title>Workforce Composition</title>
<link href="https://fonts.googleapis.com/css2?family=Bebas+Neue&family=Libre+Baskerville:wght@400&display=swap" rel="stylesheet">
<style>
  :root {
    --frame: #c4c4c4;
    --paper: #ffffff;
    --navy: #00204a;
    --sand: #dca05f;
    --taupe: #6b584c;
    --espresso: #44281a;
    --gold: #bd9457;
    --camel: #a67f56;
    --rule: #00204a;
  }
  * { margin: 0; padding: 0; box-sizing: border-box; }
  html, body { width: 1112px; height: 1200px; overflow: hidden; background: var(--frame); }
  .infographic { position: relative; width: 1112px; height: 1200px; background: var(--frame); }
  .sheet { position: absolute; left: 40px; top: 42px; width: 1038px; height: 1120px; background: var(--paper); }
  .masthead { position: absolute; left: 40px; top: 42px; width: 1038px; height: 140px; background: var(--navy); }
  .masthead__kicker {
    position: absolute; left: 52px; top: 28px;
    font-family: "Libre Baskerville", serif; font-size: 41px; line-height: 46px;
    color: var(--sand); letter-spacing: 2px;
  }
  .masthead__kicker span { display: block; letter-spacing: 7px; }
  .masthead__title {
    position: absolute; left: 295px; top: 26px;
    font-family: "Bebas Neue", sans-serif; font-size: 108px; line-height: 100px;
    color: #ececec; letter-spacing: 0.5px; white-space: nowrap;
  }
  .divider-v { position: absolute; left: 560px; top: 192px; width: 1px; height: 970px; background: var(--rule); }
  .divider-h { position: absolute; left: 67px; top: 627px; width: 985px; height: 1px; background: var(--rule); }
  .section-title {
    position: absolute; font-family: "Libre Baskerville", serif; font-size: 36px; line-height: 40px;
    color: var(--navy); white-space: nowrap; letter-spacing: 1px;
  }
  .figure { position: absolute; }
  .stat {
    position: absolute; font-family: "Bebas Neue", sans-serif; line-height: 1; white-space: nowrap;
  }
  .stat--diversity { font-size: 64px; color: var(--navy); }
  .label {
    position: absolute; font-family: "Libre Baskerville", serif; font-size: 22px; line-height: 27px;
  }
  .age-band {
    position: absolute; font-family: "Bebas Neue", sans-serif; font-size: 28px; color: var(--navy);
    transform: rotate(-90deg); transform-origin: left top; white-space: nowrap; line-height: 1;
  }
  .stat--age { font-size: 60px; }
  .legend { font-size: 40px; color: var(--taupe); }
  .callout { font-size: 42px; color: var(--taupe); }
  .board-figure { font-size: 50px; color: var(--taupe); line-height: 44px; }
  .board-note { color: var(--navy); font-size: 21px; line-height: 26px; }
</style>
</head>
<body>
<main class="infographic">
  <svg width="0" height="0" style="position:absolute" aria-hidden="true">
    <defs>
      <symbol id="person" viewBox="0 0 40 110">
        <circle cx="20" cy="10" r="10"/>
        <rect x="0" y="24" width="40" height="8" rx="3"/>
        <rect x="0" y="24" width="6" height="50" rx="3"/>
        <rect x="34" y="24" width="6" height="50" rx="3"/>
        <rect x="8" y="24" width="24" height="50" rx="2"/>
        <rect x="8" y="66" width="10" height="44" rx="5"/>
        <rect x="22" y="66" width="10" height="44" rx="5"/>
      </symbol>
      <symbol id="woman" viewBox="0 0 40 110">
        <circle cx="20" cy="10" r="10"/>
        <path d="M11 24 H29 Q33 24 34 28 L40 56 L35 58 L31 40 L38 76 H2 L9 40 L5 58 L0 56 L6 28 Q7 24 11 24 Z"/>
        <rect x="10" y="72" width="9" height="38" rx="4.5"/>
        <rect x="21" y="72" width="9" height="38" rx="4.5"/>
      </symbol>
    </defs>
  </svg>

  <div class="sheet"></div>

  <header class="masthead">
    <div class="masthead__kicker"><span>GENDER</span>CHART</div>
    <h1 class="masthead__title">25 TOTAL EMPLOYEES</h1>
  </header>

  <div class="divider-v"></div>
  <div class="divider-h"></div>

  <!-- Diversity -->
  <section class="diversity">
    <h2 class="section-title" style="left:150px;top:210px;">DIVERSITY</h2>
    <svg class="figure" style="left:87px;top:278px;" width="52" height="145"><use href="#person" fill="var(--sand)"/></svg>
    <div class="stat stat--diversity" style="left:159px;top:310px;">60%</div>
    <div class="label" style="left:160px;top:373px;color:var(--sand);">White</div>

    <svg class="figure" style="left:313px;top:278px;" width="52" height="145"><use href="#person" fill="var(--taupe)"/></svg>
    <div class="stat stat--diversity" style="left:386px;top:310px;">24%</div>
    <div class="label" style="left:387px;top:373px;color:var(--taupe);">Asian</div>

    <svg class="figure" style="left:87px;top:447px;" width="52" height="145"><use href="#person" fill="var(--espresso)"/></svg>
    <div class="stat stat--diversity" style="left:159px;top:479px;">08%</div>
    <div class="label" style="left:160px;top:542px;color:var(--espresso);">Hispanic</div>

    <svg class="figure" style="left:313px;top:447px;" width="52" height="145"><use href="#person" fill="var(--gold)"/></svg>
    <div class="stat stat--diversity" style="left:386px;top:479px;">08%</div>
    <div class="label" style="left:387px;top:542px;color:var(--gold);">Middle-<br>Eastern</div>
  </section>

  <!-- Age -->
  <section class="age">
    <h2 class="section-title" style="left:724px;top:210px;">AGE</h2>

    <div class="age-band" style="left:582px;top:357px;">25 - 44</div>
    <svg class="figure" style="left:614px;top:280px;" width="210" height="81">
      <use href="#person" x="0" width="29" height="81" fill="var(--taupe)"/>
      <use href="#person" x="44" width="29" height="81" fill="var(--taupe)"/>
      <use href="#person" x="86" width="29" height="81" fill="var(--taupe)"/>
      <use href="#person" x="128" width="29" height="81" fill="var(--taupe)"/>
      <use href="#person" x="170" width="29" height="81" fill="var(--taupe)"/>
    </svg>
    <div class="stat stat--age" style="left:831px;top:298px;color:var(--taupe);">32%</div>

    <div class="age-band" style="left:582px;top:478px;">45 - 64</div>
    <svg class="figure" style="left:614px;top:395px;" width="370" height="81">
      <use href="#person" x="0" width="29" height="81" fill="var(--gold)"/>
      <use href="#person" x="44" width="29" height="81" fill="var(--gold)"/>
      <use href="#person" x="86" width="29" height="81" fill="var(--gold)"/>
      <use href="#person" x="128" width="29" height="81" fill="var(--gold)"/>
      <use href="#person" x="170" width="29" height="81" fill="var(--gold)"/>
      <use href="#person" x="209" width="29" height="81" fill="var(--gold)"/>
      <use href="#person" x="251" width="29" height="81" fill="var(--gold)"/>
      <use href="#person" x="294" width="29" height="81" fill="var(--gold)"/>
      <use href="#person" x="336" width="29" height="81" fill="var(--gold)"/>
    </svg>
    <div class="stat stat--age" style="left:985px;top:419px;color:var(--gold);">56%</div>

    <div class="age-band" style="left:582px;top:588px;">65+</div>
    <svg class="figure" style="left:614px;top:512px;" width="80" height="81">
      <use href="#person" x="0" width="29" height="81" fill="var(--sand)"/>
      <use href="#person" x="44" width="29" height="81" fill="var(--sand)"/>
    </svg>
    <div class="stat stat--age" style="left:707px;top:536px;color:var(--sand);">12%</div>
  </section>

  <!-- Gender -->
  <section class="gender">
    <h2 class="section-title" style="left:198px;top:666px;">GENDER</h2>
    <svg class="figure" style="left:121px;top:730px;" width="324" height="324" role="img" aria-label="Pie chart: female 60%, male 40%">
      <circle cx="162" cy="162" r="162" fill="var(--taupe)"/>
      <path d="M162 162 L162 0 A162 162 0 0 0 66.8 293.1 Z" fill="var(--sand)"/>
    </svg>
    <svg class="figure" style="left:85px;top:1068px;" width="28" height="76"><use href="#woman" fill="var(--taupe)"/></svg>
    <div class="stat legend" style="left:122px;top:1094px;">FEMALE: 60%</div>
    <svg class="figure" style="left:335px;top:1064px;" width="28" height="76"><use href="#person" fill="var(--camel)"/></svg>
    <div class="stat legend" style="left:375px;top:1094px;">MALE: 40%</div>
  </section>

  <!-- Executive officers -->
  <section class="executives">
    <h2 class="section-title" style="left:586px;top:672px;">EXECUTIVE OFFICERS</h2>
    <svg class="figure" style="left:585px;top:735px;" width="160" height="107">
      <use href="#person" x="0" width="48" height="104" fill="var(--camel)"/>
      <use href="#woman" x="53" y="3" width="48" height="104" fill="var(--taupe)"/>
      <use href="#woman" x="106" y="3" width="48" height="104" fill="var(--taupe)"/>
    </svg>
    <div class="stat callout" style="left:754px;top:778px;">2 OUT OF 3 ARE WOMEN</div>
  </section>

  <!-- Board composition -->
  <section class="board">
    <h2 class="section-title" style="left:591px;top:900px;">BOARD COMPOSITION</h2>
    <svg class="figure" style="left:585px;top:967px;" width="156" height="156" role="img" aria-label="Pie chart: board 50% women">
      <path d="M78 0 A78 78 0 0 0 78 156 Z" fill="var(--camel)"/>
      <path d="M78 0 A78 78 0 0 1 78 156 Z" fill="var(--taupe)"/>
    </svg>
    <div class="stat board-figure" style="left:787px;top:959px;">50% WOMEN<br>(3 DIRECTORS)</div>
    <p class="label board-note" style="left:790px;top:1060px;">One woman from an<br>unrepresented<br>community</p>
  </section>
</main>
</body>
</html>
```